Commercial photographer, UAV drone photography & 360 walk-through visuals

I need a business card design that is minimalist but yet pretentiously creative. My target market are architects, designers, advertising agents and marketing managers. It is important to stress that though I am asking for a minimalist design it needs to have creative impact.

Target Market(s)

Architects, interiors designers, web-designers, artists

Contact Information for Business Card

Include my name, mobile [cell] number, email, web page and the company logo. Do not to include a postal address.

Colors

Designer to choose colors to be used in the design.

Requirements
Must have
• The following information is to be included:
• Miles Perrow
• Photographer
• m: 07812 593174
• e: miles@mpframeworks.co.uk
• w: mpframeworks.co.uk

```html
<!DOCTYPE html>
<html lang="en">
<head>
<meta charset="utf-8">
<title>MP Frameworks – Business Card</title>
<link rel="stylesheet" href="https://fonts.googleapis.com/css2?family=Open+Sans:wght@400;600&display=swap">
<style>
  :root {
    --backdrop: #3a3a3a;
    --card: #1f1f1f;
    --motif: #2e2e2e;
    --ink: #ffffff;
    --ink-soft: #d9d9d9;
    --icon: #bdbdbd;
  }
  * { margin: 0; padding: 0; box-sizing: border-box; }
  html, body { width: 1200px; height: 900px; overflow: hidden; }
  body {
    background: var(--backdrop);
    font-family: "Open Sans", Arial, sans-serif;
    display: flex;
    align-items: center;
    justify-content: center;
    gap: 50px;
  }
  .card {
    width: 520px;
    height: 320px;
    background: var(--card);
    border-radius: 4px;
    position: relative;
    overflow: hidden;
    color: var(--ink);
    box-shadow: 0 18px 40px rgba(0,0,0,0.45);
  }
  .card-motif {
    position: absolute;
    border-radius: 50%;
    background: var(--motif);
  }
  .brand {
    position: relative;
    display: flex;
    align-items: center;
    gap: 14px;
  }
  .brand-dot {
    width: 14px;
    height: 14px;
    border-radius: 50%;
    background: var(--ink);
    flex: none;
  }
  .brand-name {
    font-weight: 400;
    letter-spacing: 0.16em;
    text-transform: uppercase;
    color: var(--ink);
    line-height: 1.1;
  }
  .brand-name span { display: block; }

  /* Contact side */
  .card-front { padding: 40px 40px; }
  .card-front .card-motif { width: 300px; height: 300px; right: -90px; bottom: -140px; }
  .card-front .brand-name { font-size: 24px; }
  .person { position: relative; margin-top: 28px; }
  .person-name { font-size: 19px; font-weight: 600; }
  .person-role { font-size: 13px; color: var(--ink-soft); margin-top: 1px; }
  .contact-list { position: relative; list-style: none; margin-top: 14px; }
  .contact-item {
    display: flex;
    align-items: center;
    gap: 10px;
    font-size: 13px;
    color: var(--ink-soft);
    line-height: 1.65;
  }
  .contact-icon { width: 12px; height: 12px; flex: none; }

  /* Brand side */
  .card-back { display: flex; align-items: center; justify-content: flex-end; padding-right: 50px; }
  .card-back .card-motif { width: 360px; height: 360px; left: -170px; top: -60px; }
  .brand-block { position: relative; }
  .card-back .brand-name { font-size: 34px; }
  .card-back .web { font-size: 14px; color: var(--ink-soft); margin-top: 16px; letter-spacing: 0.02em; }
</style>
</head>
<body>

  <section class="card card-front" aria-label="Business card, contact side">
    <div class="card-motif" aria-hidden="true"></div>
    <div class="brand">
      <div class="brand-dot" aria-hidden="true"></div>
      <div class="brand-name"><span>MP</span><span>Frameworks</span></div>
    </div>
    <div class="person">
      <div class="person-name">Miles Perrow</div>
      <div class="person-role">Commercial Photographer</div>
    </div>
    <ul class="contact-list">
      <li class="contact-item">
        <svg class="contact-icon" viewBox="0 0 12 12" aria-hidden="true"><rect x="3" y="0.5" width="6" height="11" rx="1" fill="none" stroke="var(--icon)"/><line x1="5" y1="9.5" x2="7" y2="9.5" stroke="var(--icon)"/></svg>
        07812 593174
      </li>
      <li class="contact-item">
        <svg class="contact-icon" viewBox="0 0 12 12" aria-hidden="true"><rect x="0.5" y="2.5" width="11" height="7" fill="var(--icon)"/><polyline points="0.5,2.5 6,7 11.5,2.5" fill="none" stroke="var(--card)"/></svg>
        miles@mpframeworks.co.uk
      </li>
      <li class="contact-item">
        <svg class="contact-icon" viewBox="0 0 12 12" aria-hidden="true"><circle cx="6" cy="6" r="5.5" fill="var(--icon)"/><ellipse cx="6" cy="6" rx="2.3" ry="5.5" fill="none" stroke="var(--card)" stroke-width="0.8"/><line x1="0.5" y1="6" x2="11.5" y2="6" stroke="var(--card)" stroke-width="0.8"/></svg>
        www.mpframeworks.co.uk
      </li>
    </ul>
  </section>

  <section class="card card-back" aria-label="Business card, brand side">
    <div class="card-motif" aria-hidden="true"></div>
    <div class="brand-block">
      <div class="brand-name"><span>MP</span><span>Frameworks</span></div>
      <div class="web">www.mpframeworks.co.uk</div>
    </div>
  </section>

</body>
</html>
```